Logistics and freight company requires website

Hi, a logistic and freight company which is based in the United States needs an industry standard website for its activities. We are into forwarding and courier goods from within United States and Canada. We deliver a wide range of goods from shipping of electronics to document, clothings, etc. The proposed website should be comtemporary and youthful. I require brilliant colors for the website. The website should be the basic things of a site. There should a category for shipping electronics, clothings, documents and others( stuffs not listed within the three I mentioned).

```html
<!DOCTYPE html>
<html lang="en">
<head>
<meta charset="utf-8">
<title>Tidewell Logistics</title>
<link rel="stylesheet" href="https://fonts.googleapis.com/css2?family=Lato:wght@400;700&family=Open+Sans:wght@400;600;700&family=Raleway:wght@500;600;700&family=Montserrat:wght@400;500&display=swap">
<style>
  :root {
    --ink: #2d3e50;
    --text: #222;
    --muted: #8a8a8a;
    --accent: #17a9d1;
    --band: #ececec;
    --white: #fff;
    --tile: #f8f8f8;
    --footer: #2b3039;
    --footer-bottom: #21252c;
    --footer-text: #6f7580;
    --dark-btn: #222;
  }
  * { margin: 0; padding: 0; box-sizing: border-box; }
  html, body { width: 1200px; height: 2256px; overflow: hidden; }
  body { position: relative; background: var(--white); font-family: "Open Sans", Arial, sans-serif; color: var(--text); }
  .abs { position: absolute; }

  /* header */
  .site-header { position: absolute; left: 0; top: 0; width: 1200px; height: 89px; background: var(--white); }
  .brand { position: absolute; left: 99px; top: 28px; font-family: "Lato", sans-serif; font-weight: 700; font-size: 31px; color: var(--ink); letter-spacing: 0.2px; }
  .main-nav a { position: absolute; top: 40px; font-family: "Lato", sans-serif; font-size: 13px; color: var(--ink); text-decoration: none; letter-spacing: 0.3px; }
  .main-nav a.active { color: var(--accent); }

  /* hero */
  .hero { position: absolute; left: 0; top: 89px; width: 1200px; height: 523px; background: linear-gradient(180deg, #7fb2de 0%, #b9d3ea 38%, #8a6a5a 52%, #4a6aa0 62%, #a99f98 78%, #c9c2bd 100%); }
  .hero-caption { position: absolute; left: 99px; background: rgba(235,235,235,0.82); font-weight: 700; font-size: 20px; color: #1a1a1a; padding: 0 15px; line-height: 50px; white-space: nowrap; }
  .hero-arrow { position: absolute; top: 244px; width: 34px; height: 34px; border-radius: 50%; background: rgba(255,255,255,0.55); }
  .hero-arrow svg { position: absolute; left: 11px; top: 9px; }

  /* intro cards */
  .intro { position: absolute; left: 0; top: 612px; width: 1200px; height: 316px; background: var(--band); }
  .intro-card { position: absolute; top: 41px; width: 488px; height: 234px; background: var(--white); }
  .intro-card .photo { position: absolute; left: 21px; top: 21px; width: 223px; height: 194px; }
  .intro-card h3 { position: absolute; left: 263px; top: 17px; width: 200px; font-size: 14.5px; font-weight: 600; line-height: 21px; color: #1a1a1a; }
  .intro-card p { position: absolute; left: 263px; width: 205px; font-size: 11px; line-height: 16.5px; color: #555; }
  .btn { position: absolute; left: 263px; top: 190px; width: 86px; height: 28px; font-size: 11px; font-weight: 600; color: var(--white); text-align: center; line-height: 28px; }
  .btn-accent { background: var(--accent); }
  .btn-dark { background: var(--dark-btn); }

  /* offer */
  .offer { position: absolute; left: 0; top: 928px; width: 1200px; height: 534px; background: var(--white); }
  .section-title { position: absolute; left: 0; top: 34px; width: 1200px; text-align: center; font-family: "Raleway", sans-serif; font-weight: 600; font-size: 26px; color: #222; }
  .offer-tile { position: absolute; width: 466px; height: 145px; background: var(--tile); }
  .offer-tile .icon { position: absolute; left: 36px; top: 32px; }
  .offer-tile h4 { position: absolute; left: 131px; top: 24px; font-family: "Raleway", sans-serif; font-weight: 700; font-size: 15px; color: #222; }
  .offer-tile p { position: absolute; left: 131px; top: 56px; width: 300px; font-size: 11px; line-height: 19.5px; color: var(--muted); }
  .divider-v { position: absolute; left: 600px; width: 0; border-left: 1px dotted #999; }
  .divider-h { position: absolute; top: 290px; height: 0; border-top: 1px dotted #999; }

  /* info */
  .info { position: absolute; left: 0; top: 1462px; width: 1200px; height: 444px; background: var(--band); }
  .info-card { position: absolute; top: 56px; width: 316px; height: 332px; background: var(--white); }
  .info-card h3 { position: absolute; left: 25px; top: 16px; font-family: "Raleway", sans-serif; font-weight: 700; font-size: 21px; color: #222; }
  .news-item { position: absolute; left: 28px; width: 270px; height: 89px; }
  .news-item .thumb { position: absolute; left: 0; top: 0; width: 89px; height: 89px; }
  .news-item .date { position: absolute; left: 115px; top: 2px; font-size: 11px; color: #222; }
  .news-item .date svg { vertical-align: -2px; margin-right: 8px; }
  .news-item .title { position: absolute; left: 115px; top: 22px; width: 140px; font-family: "Raleway", sans-serif; font-weight: 600; font-size: 12.5px; line-height: 16px; color: #111; }
  .view-all { position: absolute; right: 20px; top: 300px; font-family: "Raleway", sans-serif; font-weight: 600; font-size: 11.5px; color: #222; }
  .view-all svg { vertical-align: -2px; margin-left: 4px; }
  .quote { position: absolute; left: 28px; top: 74px; width: 260px; text-align: center; font-size: 11px; line-height: 18.5px; color: #555; }
  .quote-author { position: absolute; left: 0; top: 227px; width: 316px; text-align: center; font-family: "Raleway", sans-serif; font-weight: 600; font-size: 12.5px; line-height: 19px; color: #111; }
  .map { position: absolute; left: 33px; top: 83px; width: 252px; height: 146px; background: linear-gradient(135deg, #e6e2d6 0%, #d9dcc8 45%, #c9d6e4 100%); }
  .loc-text { position: absolute; left: 28px; top: 242px; width: 260px; text-align: center; font-size: 11px; line-height: 18.5px; color: #555; }

  /* footer */
  .site-footer { position: absolute; left: 0; top: 1906px; width: 1200px; height: 239px; background: var(--footer); }
  .footer-col { position: absolute; top: 41px; font-family: "Montserrat", sans-serif; }
  .footer-col h5 { font-size: 10px; font-weight: 500; color: #e4e6ea; letter-spacing: 0.3px; margin-bottom: 11px; }
  .footer-col a { display: block; font-size: 10px; line-height: 20.5px; color: var(--footer-text); text-decoration: none; }
  .ship-label { position: absolute; left: 96px; top: 192px; font-family: "Montserrat", sans-serif; font-size: 10px; font-weight: 500; color: #e4e6ea; }
  .ship-select { position: absolute; left: 182px; top: 182px; width: 187px; height: 35px; border: 1px solid #555b66; font-family: "Montserrat", sans-serif; font-size: 10px; color: #e4e6ea; line-height: 33px; padding-left: 15px; }
  .ship-select svg { position: absolute; right: 14px; top: 15px; }
  .pay-badges { position: absolute; left: 767px; top: 188px; display: flex; gap: 4px; }
  .pay-badges span { width: 30px; height: 20px; border-radius: 2px; background: #f2f2f2; }
  .pay-badges span.alt { background: #d9dde3; }

  .footer-bottom { position: absolute; left: 0; top: 2145px; width: 1200px; height: 111px; background: var(--footer-bottom); }
  .legal-links { position: absolute; left: 0; top: 30px; width: 1200px; text-align: center; font-family: "Montserrat", sans-serif; font-size: 10px; font-weight: 500; color: #e4e6ea; }
  .legal-links a { color: inherit; text-decoration: none; margin: 0 11px; }
  .copyright { position: absolute; left: 0; top: 51px; width: 1200px; text-align: center; font-family: "Montserrat", sans-serif; font-size: 9.5px; color: var(--footer-text); }
  .social-dots { position: absolute; left: 540px; top: 81px; display: flex; gap: 40px; }
  .social-dots span { width: 8px; height: 8px; border-radius: 50%; background: #6f7580; }
</style>
</head>
<body>

<header class="site-header">
  <div class="brand">TIDEWELL LOGISTICS.</div>
  <nav class="main-nav">
    <a class="active" style="left:653px">HOME</a>
    <a style="left:735px">ABOUT US</a>
    <a style="left:844px">SERVICES</a>
    <a style="left:943px">GALLERY</a>
    <a style="left:1041px">CONTACT</a>
  </nav>
</header>

<section class="hero" role="img" aria-label="Container port with an orange gantry crane and stacked shipping containers under a blue sky">
  <div class="hero-arrow" style="left:16px"><svg width="12" height="16" viewBox="0 0 12 16"><path d="M9 2 L3 8 L9 14" fill="none" stroke="#fff" stroke-width="2"/></svg></div>
  <div class="hero-arrow" style="left:1146px"><svg width="12" height="16" viewBox="0 0 12 16"><path d="M3 2 L9 8 L3 14" fill="none" stroke="#fff" stroke-width="2"/></svg></div>
  <div class="hero-caption" style="top:362px">WE ARE A LOGISTIC AND FREIGHT COMPANY WHICH IS</div>
  <div class="hero-caption" style="top:413px;height:48px;line-height:48px">BASED IN THE UNITED STATES.</div>
</section>

<section class="intro">
  <article class="intro-card" style="left:99px">
    <div class="photo" role="img" aria-label="Hands planning a route over a paper map with a coffee cup" style="background:linear-gradient(135deg,#8f8274 0%,#c9c0b0 50%,#6f7a86 100%)"></div>
    <h3>We are into forwarding and courier goods from within United States and Canada.</h3>
    <p style="top:84px">Lorem ipsum dolor sit amet, consectetur adipiscing elit. In laoreet quam non quam lobortis facilisis. Ut eu ipsum tempor</p>
    <div class="btn btn-accent">Read More</div>
  </article>
  <article class="intro-card" style="left:614px">
    <div class="photo" role="img" aria-label="Courier in a delivery van with a wrapped parcel" style="background:linear-gradient(135deg,#3c3f44 0%,#8a8d90 55%,#c7a57a 100%)"></div>
    <h3>We deliver a wide range of goods from shipping of electronics to document, clothing's, etc</h3>
    <p style="top:105px">Lorem ipsum dolor sit amet, consectetur adipiscing elit. In laoreet quam non quam lobortis facilisis.</p>
    <div class="btn btn-dark">Read More</div>
  </article>
</section>

<section class="offer">
  <h2 class="section-title">What We Offer</h2>

  <div class="offer-tile" style="left:123px;top:111px">
    <svg class="icon" width="60" height="66" viewBox="0 0 60 66">
      <rect x="4" y="8" width="38" height="50" rx="2" fill="#4a4f57"/>
      <rect x="15" y="3" width="16" height="9" rx="2" fill="#4a4f57" stroke="#f8f8f8" stroke-width="2"/>
      <rect x="11" y="20" width="24" height="3" fill="#f8f8f8"/>
      <rect x="11" y="29" width="24" height="3" fill="#f8f8f8"/>
      <rect x="11" y="38" width="16" height="3" fill="#f8f8f8"/>
      <circle cx="44" cy="48" r="12" fill="#17a9d1" stroke="#f8f8f8" stroke-width="2"/>
      <path d="M38 48 L43 53 L51 43" fill="none" stroke="#fff" stroke-width="3"/>
    </svg>
    <h4>Contract logistics</h4>
    <p>Need custom logistic service? We got it covered. From overland, air, rail and sea transportation. Fast, safe and accurate shipment provided all over the globe.</p>
  </div>

  <div class="offer-tile" style="left:618px;top:111px">
    <svg class="icon" width="70" height="60" viewBox="0 0 70 60">
      <circle cx="24" cy="30" r="20" fill="none" stroke="#4a4f57" stroke-width="4"/>
      <ellipse cx="24" cy="30" rx="8" ry="20" fill="none" stroke="#4a4f57" stroke-width="3"/>
      <path d="M5 23 H43 M5 37 H43" stroke="#4a4f57" stroke-width="3"/>
      <path d="M30 32 L68 30 L68 34 L30 36 Z M46 31 L40 18 L46 18 L56 31 Z M46 35 L40 48 L46 48 L56 35 Z M32 33 L30 26 L34 26 L38 33 Z" fill="#17a9d1"/>
    </svg>
    <h4>Overland, Ocean and Air Freight</h4>
    <p>Trucking company offers the best logistics services using all mens of supply chain. Use our overland, ocean and air freight solutions for shipment of your goods.</p>
  </div>

  <div class="offer-tile" style="left:123px;top:320px">
    <svg class="icon" width="70" height="60" viewBox="0 0 70 60">
      <rect x="4" y="20" width="40" height="24" rx="3" fill="#17a9d1"/>
      <path d="M12 20 V4 H30 L36 20" fill="none" stroke="#4a4f57" stroke-width="4"/>
      <rect x="46" y="4" width="4" height="44" fill="#4a4f57"/>
      <rect x="50" y="42" width="16" height="4" fill="#4a4f57"/>
      <rect x="54" y="28" width="10" height="12" fill="#17a9d1"/>
      <circle cx="13" cy="47" r="7" fill="#4a4f57" stroke="#f8f8f8" stroke-width="2"/>
      <circle cx="36" cy="47" r="7" fill="#4a4f57" stroke="#f8f8f8" stroke-width="2"/>
    </svg>
    <h4>Warehousing and Storage</h4>
    <p>Trucking offers intelligent warehouse solution. Lower your storage and good maintenance by using our modern and intelligent warehouses. You can see all locations on location page.</p>
  </div>

  <div class="offer-tile" style="left:618px;top:320px">
    <svg class="icon" width="70" height="62" viewBox="0 0 70 62">
      <rect x="4" y="4" width="46" height="32" rx="3" fill="none" stroke="#4a4f57" stroke-width="4"/>
      <rect x="22" y="36" width="10" height="8" fill="#4a4f57"/>
      <rect x="14" y="44" width="26" height="4" fill="#4a4f57"/>
      <path d="M40 24 C40 20 46 20 46 24 V34 C46 30 52 30 52 34 C52 30 58 30 58 34 C58 31 64 31 64 35 V48 C64 55 58 60 52 60 H48 C42 60 38 54 34 48 L30 42 C28 38 33 35 36 39 L40 44 Z" fill="#17a9d1"/>
    </svg>
    <h4>Consulting Services</h4>
    <p>Don't know what mean of transportation would be right for you, or you need someone for full supply chain management? Please contact us. Our team of professionals will be happy to help.</p>
  </div>

  <div class="divider-v" style="top:122px;height:134px"></div>
  <div class="divider-v" style="top:302px;height:106px"></div>
  <div class="divider-h" style="left:165px;width:422px"></div>
  <div class="divider-h" style="left:614px;width:430px"></div>
</section>

<section class="info">
  <article class="info-card" style="left:99px">
    <h3>Latest News</h3>
    <div class="news-item" style="top:75px">
      <div class="thumb" role="img" aria-label="Port worker in red overalls beside containers" style="background:linear-gradient(160deg,#6e93c0 0%,#c2473f 55%,#7d8591 100%)"></div>
      <div class="date"><svg width="12" height="12" viewBox="0 0 12 12"><rect x="0.5" y="1.5" width="11" height="10" fill="none" stroke="#333"/><path d="M0.5 4.5 H11.5 M3 0 V3 M9 0 V3 M3 7 H5 M7 7 H9" stroke="#333"/></svg>Jan - 22 - 2016</div>
      <div class="title">Lorem ipsum dolor sit amet, consectetur adipiscing elit.</div>
    </div>
    <div class="news-item" style="top:188px">
      <div class="thumb" role="img" aria-label="Container terminal at dusk with cranes and lights" style="background:linear-gradient(160deg,#3f4f78 0%,#9a5b6a 55%,#d69a4e 100%)"></div>
      <div class="date"><svg width="12" height="12" viewBox="0 0 12 12"><rect x="0.5" y="1.5" width="11" height="10" fill="none" stroke="#333"/><path d="M0.5 4.5 H11.5 M3 0 V3 M9 0 V3 M3 7 H5 M7 7 H9" stroke="#333"/></svg>Jan - 22 - 2016</div>
      <div class="title">Dolor sit amet, consectetur adipiscing elit. In laoreet quam</div>
    </div>
    <div class="view-all">View All<svg width="12" height="12" viewBox="0 0 12 12"><circle cx="6" cy="6" r="5.3" fill="none" stroke="#222"/><path d="M3.5 6 H8 M6 4 L8 6 L6 8" fill="none" stroke="#222"/></svg></div>
  </article>

  <article class="info-card" style="left:442px">
    <h3>Client Testimonials</h3>
    <p class="quote">Donec ut nulla ligula. Vestibulum ante ipsum primis in faucibus orci luctus et ultrices posuere cubilia Curae; Integer id viverra tellus. Phasellus pretium accumsan justo, pharetra ex. Proin luctus orci id justo laoreet, nec tempor ante feugiat. Ut ut porta arcu, nec elementum nisi. Phasellus turpis purus, consectetur eu purus eget, fermentum</p>
    <div class="quote-author">Jhone Doe<br>Lorem Ipsum DOlor Sit</div>
    <div class="view-all">View All<svg width="12" height="12" viewBox="0 0 12 12"><circle cx="6" cy="6" r="5.3" fill="none" stroke="#222"/><path d="M3.5 6 H8 M6 4 L8 6 L6 8" fill="none" stroke="#222"/></svg></div>
  </article>

  <article class="info-card" style="left:785px">
    <h3>Our Locations</h3>
    <div class="map" role="img" aria-label="Street map of the office area with a location pin"></div>
    <p class="loc-text">Donec ut nulla ligula. Vestibulum ante ipsum primis in faucibus orci luctus et ultrices posuere cubilia Curae;</p>
  </article>
</section>

<footer class="site-footer">
  <div class="footer-col" style="left:96px"><h5>QUESTIONS?</h5><a>Help</a><a>Track Order</a><a>Returns</a></div>
  <div class="footer-col" style="left:307px"><h5>WHAT'S IN STORE</h5><a>Help</a><a>Track Order</a><a>Returns</a></div>
  <div class="footer-col" style="left:517px"><h5>FOLLOW US</h5><a>Social Feed</a><a>Microblog</a><a>Community</a><a>Photo Stream</a></div>
  <div class="footer-col" style="left:725px"><h5>MORE ABOUT</h5><a>Corporate Responsibility</a><a>Jobs at</a><a>Lorem</a><a>As Seen On Screen</a></div>
  <div class="footer-col" style="left:932px"><h5>Useful Links</h5><a>Mobile and apps</a><a>Marketplace</a></div>

  <div class="ship-label">SHIPPING TO:</div>
  <div class="ship-select">USA<svg width="7" height="4" viewBox="0 0 7 4"><path d="M0 0 H7 L3.5 4 Z" fill="#e4e6ea"/></svg></div>

  <div class="pay-badges">
    <span></span><span class="alt"></span><span></span><span class="alt"></span><span></span><span class="alt"></span><span></span><span class="alt"></span><span></span>
  </div>
</footer>

<div class="footer-bottom">
  <div class="legal-links"><a>PRIVACY &amp; COOKIES</a><a>TERMS &amp; CONDITIONS</a><a>STORE DIRECTORY</a><a>ABOUT US</a></div>
  <div class="copyright">Copyrights 2016 © yoursite All Rights Reserved</div>
  <div class="social-dots"><span></span><span></span><span></span><span></span></div>
</div>

</body>
</html>
```